Copper Wagon
ideas, energy & innovation
Can you also please upload drafts of the letter headed paper, compliments slips and invoice drafts for me to also look at!

```html
<!DOCTYPE html>
<html lang="en">
<head>
<meta charset="utf-8">
<title>Copper Wagon – Stationery Set</title>
<link href="https://fonts.googleapis.com/css2?family=Open+Sans:wght@400;600;700&display=swap" rel="stylesheet">
<style>
:root{
  --bg:#ffffff;
  --ink:#2b2b2b;
  --muted:#8a8a8a;
  --blue:#1b4c9c;
  --blue-light:#3b8ad6;
  --blue-pale:#dbe7f6;
  --green:#7cc242;
  --orange:#f2691c;
  --paper:#ffffff;
  --shadow:0 1px 3px rgba(0,0,0,.35);
}
*{box-sizing:border-box;margin:0;padding:0}
html,body{width:1200px;height:425px;overflow:hidden;background:var(--bg);font-family:"Open Sans",Arial,sans-serif;color:var(--ink)}
.sheet{position:relative;width:1200px;height:425px}
.item{position:absolute;box-shadow:var(--shadow);overflow:hidden}
.label{position:absolute;font-size:6px;color:var(--muted);text-align:center}
.brand{display:flex;align-items:center;gap:4px;font-weight:700;color:var(--blue);white-space:nowrap}
.brand .dot{border-radius:50%;background:var(--blue-light)}
.tiny{font-size:4.5px;line-height:6px;color:#555}
.swoosh{position:absolute;left:0;bottom:0;width:100%;z-index:1}

/* business cards */
.card{width:166px;height:96px;left:19px}
.card-front{top:43px;background:var(--paper)}
.card-front .brand{position:absolute;left:8px;top:10px;font-size:11px}
.card-front .brand .dot{width:12px;height:12px}
.card-front .person{position:absolute;right:10px;top:32px;text-align:right}
.card-front .person b{display:block;font-size:5.5px;color:var(--blue)}
.card-back{top:163px;background:linear-gradient(160deg,#2f7fd0,#123e8a)}
.card-back .brand{position:absolute;left:50%;top:38px;transform:translateX(-50%);font-size:10px;color:#fff}
.card-back .brand .dot{width:10px;height:10px;background:#fff}
.card-back .tag{position:absolute;width:100%;top:56px;text-align:center;font-size:5px;color:#cfe2f7}
.card-alt{top:283px;background:linear-gradient(160deg,#2b73c6,#0f3479)}
.card-alt .mark{position:absolute;left:48px;top:14px;width:70px;height:70px;border-radius:50%;background:rgba(255,255,255,.12)}

/* letterhead */
.letterhead{left:204px;top:19px;width:276px;height:365px;background:var(--paper)}
.letterhead .brand{position:absolute;left:10px;top:12px;font-size:11px}
.letterhead .brand .dot{width:12px;height:12px}
.letterhead .contact{position:absolute;right:12px;top:12px}
.letterhead .footer{position:absolute;left:14px;bottom:12px;font-size:4.5px;line-height:6px;color:#fff;white-space:nowrap;z-index:3}

/* envelopes */
.envelope{left:492px;width:336px;height:140px}
.env-1{top:48px;background:var(--orange);z-index:1}
.env-2{top:92px;background:var(--green);z-index:2}
.env-3{top:136px;background:var(--blue-light);z-index:3}
.env-4{top:188px;background:#f4f4f4;z-index:4}
.env-5{top:244px;background:var(--paper);z-index:5}
.envelope svg{position:absolute;inset:0}
.env-5 .brand{position:absolute;left:10px;top:10px;font-size:9px}
.env-5 .brand .dot{width:10px;height:10px}
.env-5 .mark{position:absolute;right:26px;top:40px;width:86px;height:86px;border-radius:50%;background:var(--blue-pale);opacity:.6}

/* invoice */
.invoice{left:888px;top:19px;width:288px;height:389px;background:var(--paper);padding:12px 14px}
.invoice .brand{font-size:11px}
.invoice .brand .dot{width:12px;height:12px}
.invoice .contact{position:absolute;right:14px;top:12px}
.invoice .fields{display:flex;justify-content:space-between;margin-top:18px;font-size:4.5px;color:#555}
.invoice .fields span{display:block;border-bottom:.5px solid #bbb;width:110px;padding-bottom:2px;margin-bottom:6px}
.line-items{width:100%;border-collapse:collapse;margin-top:10px;font-size:4.5px}
.line-items th{background:var(--blue);color:#fff;font-weight:600;text-align:left;padding:2px 3px;height:9px}
.line-items td{height:9.5px;border:.5px solid #c9d8ee}
.line-items tr:nth-child(even) td{background:var(--blue-pale)}
.totals{margin-top:6px;margin-left:auto;width:90px;font-size:4.5px}
.totals div{display:flex;justify-content:space-between;border-bottom:.5px solid #bbb;padding:1.5px 0}
.invoice .note{position:absolute;left:14px;bottom:12px}
</style>
</head>
<body>
<main class="sheet">

  <!-- business cards -->
  <section class="item card card-front">
    <div class="brand"><span class="dot"></span>CopperWagon</div>
    <div class="person tiny"><b>Ellen Marsh</b>Creative Director<br>T 0123 456 789<br>ellen@copperwagon.com</div>
    <svg class="swoosh" viewBox="0 0 166 30" height="30" preserveAspectRatio="none">
      <path d="M0 18 Q80 4 166 10 L166 30 L0 30Z" fill="var(--green)"/>
      <path d="M0 22 Q80 8 166 15 L166 30 L0 30Z" fill="var(--blue)"/>
    </svg>
  </section>
  <p class="label" style="left:19px;top:142px;width:166px">Business Card Front</p>

  <section class="item card card-back">
    <div class="brand"><span class="dot"></span>CopperWagon</div>
    <p class="tag">ideas, energy &amp; innovation</p>
  </section>
  <p class="label" style="left:19px;top:262px;width:166px">Business Card Back</p>

  <section class="item card card-alt">
    <div class="mark" role="img" aria-label="Faint brand mark decoration"></div>
  </section>
  <p class="label" style="left:19px;top:382px;width:166px">Business Card Back Alt</p>

  <!-- letterhead -->
  <section class="item letterhead">
    <div class="brand"><span class="dot"></span>CopperWagon</div>
    <div class="contact tiny">T 0123 456 789<br>F 0123 456 790<br>hello@copperwagon.com<br>www.copperwagon.com</div>
    <svg class="swoosh" viewBox="0 0 276 70" height="70" preserveAspectRatio="none">
      <path d="M0 30 Q140 0 276 22 L276 70 L0 70Z" fill="var(--green)"/>
      <path d="M0 38 Q140 8 276 30 L276 70 L0 70Z" fill="var(--blue)"/>
    </svg>
    <p class="footer">14 Harbour Lane, Millbrook, MB4 2XY</p>
  </section>
  <p class="label" style="left:204px;top:387px;width:276px">Letterhead</p>

  <!-- envelopes -->
  <section class="item envelope env-1">
    <svg viewBox="0 0 336 140" preserveAspectRatio="none"><path d="M0 0 L168 58 L336 0" fill="rgba(0,0,0,.12)" stroke="rgba(255,255,255,.5)" stroke-width="1"/></svg>
  </section>
  <section class="item envelope env-2">
    <svg viewBox="0 0 336 140" preserveAspectRatio="none"><path d="M0 0 L168 58 L336 0" fill="rgba(0,0,0,.12)" stroke="rgba(255,255,255,.5)" stroke-width="1"/></svg>
  </section>
  <section class="item envelope env-3">
    <svg viewBox="0 0 336 140" preserveAspectRatio="none"><path d="M0 0 L168 58 L336 0" fill="rgba(0,0,0,.12)" stroke="rgba(255,255,255,.5)" stroke-width="1"/></svg>
  </section>
  <section class="item envelope env-4">
    <svg viewBox="0 0 336 140" preserveAspectRatio="none"><path d="M0 0 L168 58 L336 0" fill="rgba(0,0,0,.05)" stroke="#ccc" stroke-width="1"/></svg>
  </section>
  <section class="item envelope env-5">
    <div class="brand"><span class="dot"></span>CopperWagon</div>
    <div class="mark" role="img" aria-label="Faint brand mark decoration"></div>
  </section>
  <p class="label" style="left:492px;top:387px;width:336px">Envelope Options</p>

  <!-- invoice -->
  <section class="item invoice">
    <div class="brand"><span class="dot"></span>CopperWagon</div>
    <div class="contact tiny">T 0123 456 789<br>hello@copperwagon.com<br>14 Harbour Lane<br>Millbrook MB4 2XY</div>
    <div class="fields">
      <div><span>Invoice No:</span><span>Bill To:</span><span>&nbsp;</span></div>
      <div><span>Date:</span><span>Terms:</span></div>
    </div>
    <table class="line-items">
      <thead><tr><th style="width:12%">Qty</th><th>Description</th><th style="width:18%">Unit Price</th><th style="width:16%">Total</th></tr></thead>
      <tbody>
        <tr><td></td><td></td><td></td><td></td></tr><tr><td></td><td></td><td></td><td></td></tr>
        <tr><td></td><td></td><td></td><td></td></tr><tr><td></td><td></td><td></td><td></td></tr>
        <tr><td></td><td></td><td></td><td></td></tr><tr><td></td><td></td><td></td><td></td></tr>
        <tr><td></td><td></td><td></td><td></td></tr><tr><td></td><td></td><td></td><td></td></tr>
        <tr><td></td><td></td><td></td><td></td></tr><tr><td></td><td></td><td></td><td></td></tr>
        <tr><td></td><td></td><td></td><td></td></tr><tr><td></td><td></td><td></td><td></td></tr>
        <tr><td></td><td></td><td></td><td></td></tr><tr><td></td><td></td><td></td><td></td></tr>
        <tr><td></td><td></td><td></td><td></td></tr><tr><td></td><td></td><td></td><td></td></tr>
        <tr><td></td><td></td><td></td><td></td></tr><tr><td></td><td></td><td></td><td></td></tr>
      </tbody>
    </table>
    <div class="totals">
      <div><span>Subtotal</span><span></span></div>
      <div><span>Tax</span><span></span></div>
      <div><span>Total</span><span></span></div>
    </div>
    <p class="note tiny">Thank you for your business.<br>Payment due within 30 days.</p>
  </section>

</main>
</body>
</html>
```